Korvane 24/7 Gym & Health Bar Webpage

We need a professional and interactive webpage for a 24/7 health club.
Our approach is professional yet friendly offering holitic professional services for both general and special populations, along with flexible 24/7 gym and group fitness memberships. Professional services that we offer;
Exercise Physiologist
Strength & Conditioning
Physiotherapy
Chiropractor
Nutrition
Personal Training
we also service acute and chronic injuries, work cover, and veteran affairs

We also have a well-being bar offers healthy food, beverages and wide range of supplements.
We send out regular newsletters and want it to be interactive with social media and e-commerce.
Final design should demonstrate a holistic approach where clients have access to a wide range of health services within a professional health club environment. needs to be phone and table friendly please

i have attached a template i had been working on but wasn't happy with it

Target Market(s)

wide demographic including:

Special population - older demographic looking for professional services. Doctors will be referring clients to us also

24/7 gym - aged 25+ yrs, male and female

Industry/Entity Type

Health And Wellness

Coding

Coded - Design and coding required

Number of Pages Required

5+ page

Colors
33a6d7
add136
ffffff
0355a3

Requirements
Must have
• atmosphere and professionalism whilst inviting and sincere
• social media interaction & blog page
• clear navigation
• mobile and table friendly
• Brisk E-newsletter sign up
• testimonials
Nice to have
• customer feedback option
• FAQ
• opportunity to integrate online shop
• ability to download free visit pass

```html
<!DOCTYPE html>
<html lang="en">
<head>
<meta charset="utf-8">
<title>Korvane 24/7 Gym &amp; Health Bar</title>
<link rel="stylesheet" href="https://fonts.googleapis.com/css2?family=Jura:wght@400;500;600&family=Lato:wght@400;700&display=swap">
<style>
  :root {
    --blue: #0355a3;
    --cyan: #33a6d7;
    --lime: #add136;
    --white: #ffffff;
    --ink: #444444;
    --grey-bg: #eeeeee;
    --black: #0a0a0a;
  }
  * { box-sizing: border-box; margin: 0; padding: 0; }
  html, body { width: 745px; height: 1200px; overflow: hidden; }
  body { position: relative; background: var(--grey-bg); font-family: "Lato", sans-serif; color: var(--ink); }
  .abs { position: absolute; }
  .display { font-family: "Jura", sans-serif; }

  .site-header { left: 0; top: 0; width: 745px; height: 98px; background: var(--white); }
  .brand { left: 48px; top: 20px; display: flex; align-items: center; gap: 8px; }
  .brand-mark { width: 44px; height: 44px; border-radius: 50%; background: var(--blue); }
  .brand-name { font-family: "Jura", sans-serif; font-weight: 600; font-size: 34px; color: var(--blue); letter-spacing: 1px; }
  .main-nav a { position: absolute; top: 38px; font-family: "Jura", sans-serif; font-weight: 500; font-size: 12.5px; color: #555; text-decoration: none; }
  .main-nav a.active { color: var(--cyan); }

  .hero { left: 0; top: 98px; width: 745px; height: 420px; background: linear-gradient(110deg, #2a2a2a 0%, #6d6d6d 35%, #9a9a9a 55%, #3a3a3a 80%, #1c1c1c 100%); }
  .round-arrow { width: 38px; height: 38px; border-radius: 50%; background: rgba(230,230,230,.85); }

  .content-panel { left: 48px; top: 446px; width: 651px; height: 582px; background: var(--white); border-top: 12px solid var(--lime); }
  .welcome-title { left: 62px; top: 466px; font-size: 27px; color: var(--blue); font-weight: 500; }
  .welcome-text { left: 62px; top: 506px; width: 618px; font-size: 9.5px; line-height: 14.4px; }
  .btn { display: flex; align-items: center; justify-content: center; background: var(--blue); color: var(--white); font-size: 11px; font-weight: 700; }
  .btn-read { left: 61px; top: 562px; width: 91px; height: 26px; }

  .service-card { top: 610px; width: 181px; height: 181px; border: 1px solid #d3d3d3; background: var(--white); }
  .service-photo { position: absolute; left: 6px; top: 6px; width: 168px; height: 91px; }
  .service-text { position: absolute; left: 9px; top: 104px; width: 165px; font-size: 9.2px; line-height: 14.4px; color: #666; }
  .service-label { position: absolute; left: -1px; bottom: -1px; width: 181px; height: 26px; background: var(--blue); color: var(--white); font-family: "Jura", sans-serif; font-weight: 600; font-size: 13px; padding: 4px 9px; }

  .section-title { font-size: 24px; color: var(--blue); font-weight: 500; }
  .client-photo { left: 63px; top: 874px; width: 78px; height: 78px; border-radius: 50%; background: radial-gradient(circle at 50% 45%, #d9a98a, #8a4a2a 75%); }
  .quote { left: 155px; top: 874px; width: 185px; font-size: 9.4px; line-height: 14.4px; color: #666; }
  .quote-by { left: 155px; top: 946px; font-size: 9px; font-weight: 700; color: #333; }
  .dot { top: 979px; width: 12px; height: 12px; border-radius: 50%; background: #000; }
  .divider { left: 353px; top: 828px; width: 6px; height: 178px; background: linear-gradient(90deg, #e4e4e4, transparent); }
  .news-text { left: 382px; top: 855px; width: 300px; font-size: 9px; line-height: 14px; color: #333; }
  .field { left: 382px; width: 272px; height: 22px; border: 1px solid #cfcfcf; font-size: 9px; color: #444; padding: 5px 8px; }
  .btn-news { left: 383px; top: 974px; width: 91px; height: 25px; }

  .promo-band { left: 48px; top: 1028px; width: 651px; height: 80px; background: var(--lime); }
  .promo-title { left: 69px; top: 1048px; font-size: 27px; color: var(--white); font-weight: 500; }
  .promo-label { left: 346px; top: 1036px; font-size: 15px; font-weight: 600; color: #111; }
  .btn-download { left: 345px; top: 1067px; width: 109px; height: 32px; font-size: 13px; font-weight: 600; font-family: "Jura", sans-serif; }
  .promo-photo { left: 534px; top: 1028px; width: 165px; height: 80px; background: linear-gradient(90deg, rgba(173,209,54,0), #6b4a3a 30%, #3a2a22 60%, #8a6a55); }

  .site-footer { left: 0; top: 1070px; width: 745px; height: 130px; background: var(--black); z-index: -1; }
  .footer-nav a { position: absolute; top: 1131px; font-size: 11.5px; color: var(--white); text-decoration: none; }
  .footer-nav a.active { color: var(--lime); }
  .social { top: 1130px; width: 14px; height: 14px; border-radius: 50%; border: 1.5px solid var(--white); }
  .copyright { left: 0; top: 1164px; width: 745px; text-align: center; font-size: 8.5px; color: var(--white); }
  .copyright span { color: var(--lime); }
</style>
</head>
<body>
  <div class="site-footer abs"></div>

  <header class="site-header abs">
    <div class="brand abs"><span class="brand-mark"></span><span class="brand-name">Korvane</span></div>
    <nav class="main-nav">
      <a class="active" style="left:255px">HOME</a>
      <a style="left:302px">ABOUT</a>
      <a style="left:360px">SERVICES</a>
      <a style="left:430px">EVENT</a>
      <a style="left:581px">CLASSES</a>
      <a style="left:646px">CONTACT</a>
    </nav>
  </header>

  <div class="hero abs" role="img" aria-label="Personal trainer spotting a woman lifting dumbbells on a bench in a gym"></div>
  <svg class="round-arrow abs" style="left:10px;top:225px" viewBox="0 0 38 38"><path d="M22 11 L15 19 L22 27" fill="none" stroke="#333" stroke-width="1.6"/></svg>
  <svg class="round-arrow abs" style="left:699px;top:225px" viewBox="0 0 38 38"><path d="M16 11 L23 19 L16 27" fill="none" stroke="#333" stroke-width="1.6"/></svg>

  <main>
    <div class="content-panel abs"></div>
    <h1 class="welcome-title display abs">Welcome</h1>
    <p class="welcome-text abs">Lorem Ipsum is simply dummy text of the printing and typesetting industry. Lorem Ipsum has been the industry's standard dummy text ever since the 1500s, when an unknown printer took a galley of type and scrambled it to make a type specimen book.Lorem Ipsum is simply dummy text of the printing and typesetting industry.</p>
    <a class="btn btn-read abs">READ MORE</a>

    <svg class="abs" style="left:20px;top:693px" width="14" height="26" viewBox="0 0 14 26"><path d="M11 2 L3 13 L11 24" fill="none" stroke="#111" stroke-width="1.8"/></svg>
    <svg class="abs" style="left:712px;top:693px" width="14" height="26" viewBox="0 0 14 26"><path d="M3 2 L11 13 L3 24" fill="none" stroke="#111" stroke-width="1.8"/></svg>

    <article class="service-card abs" style="left:61px">
      <div class="service-photo" role="img" aria-label="Trainer coaching a woman with a kettlebell in a gym" style="background:linear-gradient(135deg,#cfd6dc,#7a8088 60%,#2c2c2c)"></div>
      <p class="service-text">Lorem Ipsum is simply dummy text of the printing and typesetting industry. Lorem Ipsum.</p>
      <div class="service-label">Exercise Physiologist</div>
    </article>
    <article class="service-card abs" style="left:284px">
      <div class="service-photo" role="img" aria-label="Athletic woman in a boxing stance" style="background:radial-gradient(circle at 50% 45%,#7a5a48,#1e1a18 75%)"></div>
      <p class="service-text">Lorem Ipsum is simply dummy text of the printing and typesetting industry. Lorem Ipsum.</p>
      <div class="service-label">Strength &amp; Conditioning</div>
    </article>
    <article class="service-card abs" style="left:504px">
      <div class="service-photo" role="img" aria-label="Physiotherapist treating a patient's knee" style="background:linear-gradient(135deg,#f4f4f4,#e8c5ac 50%,#9fb7d6)"></div>
      <p class="service-text">Lorem Ipsum is simply dummy text of the printing and typesetting industry. Lorem Ipsum.</p>
      <div class="service-label">Physiotherapy</div>
    </article>

    <section>
      <h2 class="section-title display abs" style="left:62px;top:818px">What our client say</h2>
      <div class="client-photo abs" role="img" aria-label="Portrait of a client"></div>
      <p class="quote abs">Lorem Ipsum is simply dummy text of the printing and typesetting industry. Lorem Ipsum has been the industry's standard dummy text ever since the 1500.</p>
      <p class="quote-by abs">By Client Name</p>
      <span class="dot abs" style="left:69px;background:var(--blue)"></span>
      <span class="dot abs" style="left:95px"></span>
      <span class="dot abs" style="left:121px"></span>
      <span class="dot abs" style="left:147px"></span>
    </section>

    <div class="divider abs"></div>

    <section>
      <h2 class="section-title display abs" style="left:380px;top:818px">Subscribe to Newsletter</h2>
      <p class="news-text abs">Lorem Ipsum is simply dummy text of the printing and typesetting industry. Lorem Ipsum has been the industry's standard.</p>
      <div class="field abs" style="top:893px">Enter your Name</div>
      <div class="field abs" style="top:932px">Enter your Email</div>
      <a class="btn btn-news abs">READ MORE</a>
    </section>

    <div class="promo-band abs"></div>
    <svg class="abs" style="left:48px;top:1028px" width="274" height="80" viewBox="0 0 274 80">
      <polygon points="0,0 250,0 274,40 250,80 0,80" fill="var(--cyan)"/>
      <polygon points="0,0 244,0 264,40 244,80 0,80" fill="var(--blue)"/>
    </svg>
    <div class="promo-title display abs">24/7 Health Club</div>
    <div class="promo-label display abs">FREE VISIT PASS</div>
    <a class="btn btn-download abs">DOWNLOAD</a>
    <div class="promo-photo abs" role="img" aria-label="Toned torsos of a woman and a man"></div>
  </main>

  <footer>
    <nav class="footer-nav">
      <a class="active" style="left:50px">Home</a>
      <a style="left:111px">About</a>
      <a style="left:172px">Services</a>
      <a style="left:238px">Testimonial</a>
      <a style="left:322px">Blog</a>
      <a style="left:364px">Contact</a>
    </nav>
    <span class="social abs" style="left:582px;border-color:var(--lime)"></span>
    <span class="social abs" style="left:627px"></span>
    <span class="social abs" style="left:681px"></span>
    <p class="copyright abs">© <span>Korvane Health &amp; Fitness</span> - 2015. All Rights Reserved.</p>
  </footer>
</body>
</html>
```